Medical VIP club - small design

Please read the specs in a design brief attached. Also we don't have logo in a Vector format and attaching the only version we have.

Industry/Entity Type

Club

```html
<!DOCTYPE html>
<html lang="en">
<head>
<meta charset="utf-8">
<title>Veranta Medical VIP Club</title>
<link rel="stylesheet" href="https://fonts.googleapis.com/css2?family=Arimo:ital,wght@0,400;0,700;1,700&family=Open+Sans:ital,wght@1,700&display=swap">
<style>
:root{
  --dark:#1f1616;
  --strip:#333333;
  --orange:#f7a41e;
  --orange-deep:#f08d1a;
  --rule:#f0913a;
  --blue:#1f5fb4;
  --blue-rule:#b5c8f2;
  --text:#6e6e6e;
  --head:#555555;
  --page:#f3f3f3;
  --white:#ffffff;
}
*{margin:0;padding:0;box-sizing:border-box}
html,body{width:1088px;height:1200px;overflow:hidden}
body{position:relative;background:var(--page);font-family:"Arimo",Arial,sans-serif;color:var(--text);font-size:9.5px;line-height:1.3}
.abs{position:absolute}
.topbar{left:0;top:0;width:1088px;height:42px;background:var(--dark)}
.login{left:378px;top:4px;color:#fff}
.login strong{font-size:12px;display:block}
.login span{font-size:7.5px;display:block;width:280px;line-height:1.35}
.search{left:806px;top:12px;width:134px;height:19px;border-radius:10px;background:#fff;border:1px solid #bbb;font-size:8px;color:#888;padding:3px 10px}
.search svg{position:absolute;right:6px;top:2px}
.hero{left:0;top:44px;width:1088px;height:261px;background:linear-gradient(90deg,#f6a423,#fbb73a 50%,#f5a020)}
.photo{left:358px;top:44px;width:592px;height:261px;background:radial-gradient(ellipse at 45% 55%,#f6e8d8 0%,#e9c49a 35%,#f4ad4b 70%,#f7a62a 100%)}
.panel{left:139px;top:0;width:219px;height:320px;background:var(--white);border-radius:0 0 8px 8px;box-shadow:0 2px 4px rgba(0,0,0,.15)}
.logo-cap{left:136px;top:0;width:228px;height:108px;background:#fff;border-radius:0 0 60% 60%/0 0 30% 30%;box-shadow:0 4px 6px rgba(0,0,0,.18)}
.brand{left:172px;top:34px;display:flex;align-items:center;gap:6px;color:var(--blue);font-weight:700;font-size:30px}
.brand i{display:block;width:14px;height:14px;border-radius:50%;background:var(--blue)}
.nav{left:150px;width:197px;height:32px;border:1px solid #ccc;border-radius:5px;background:linear-gradient(#fafafa,#e6e6e6);font-weight:700;font-size:11px;color:#333;padding:10px 0 0 18px}
.nav svg{position:absolute;right:9px;top:7px}
.strip{left:0;top:305px;width:1088px;height:25px;background:var(--strip)}
.connect{left:820px;top:311px;width:98px;height:15px;background:#3b5997;color:#fff;font-size:8px;font-weight:700;padding:2px 0 0 18px;white-space:nowrap}
.connect i{position:absolute;left:4px;top:2px;width:10px;height:11px;background:#fff}
.dot-blue{left:922px;top:297px;width:24px;height:24px;border-radius:50%;background:#3a97e0}
.services{left:136px;top:330px;width:816px;height:150px;display:flex;background:linear-gradient(#fff,#f2f2f2)}
.svc{flex:1;border-left:1px solid #b8c6e0;padding:8px 0 0 16px;font-weight:700;font-size:14px;color:#555;position:relative}
.svc:last-child{border-right:1px solid #b8c6e0}
.svc .ico{position:absolute;left:50%;top:58px;margin-left:-28px;width:56px;height:56px;border-radius:8px}
.h2{font-size:16px;font-weight:700;color:var(--head)}
.rule{height:5px;background:var(--rule)}
.lead{font-weight:700;font-size:10.5px;color:#666}
.news-name{font-weight:700;font-size:11px;color:#555}
.subhead{font-family:"Open Sans",sans-serif;font-style:italic;font-weight:700;color:#666}
.email{left:692px;top:790px;width:198px;height:24px;border:1px solid #999;background:#fff;font-size:8.5px;padding:5px 6px}
.email i{position:absolute;right:6px;top:3px;width:16px;height:16px;border-radius:50%;background:var(--orange-deep)}
.apply{left:825px;top:820px;width:65px;height:25px;border-radius:6px;background:linear-gradient(#a9cdf0,#5c97d6);border:1px solid #4d7fb8;color:#fff;font-weight:700;font-size:13px;text-align:center;padding-top:4px}
.gallery{left:164px;top:880px;display:flex;gap:4px}
.gallery div{width:148px;height:98px}
.arrow{width:19px;height:19px}
.footer{left:0;top:1000px;width:1088px;height:180px;background:linear-gradient(#e3e3e3,#f4f4f4);border-top:2px solid #cfcfcf}
.fh{font-size:14px}
.social{display:flex;gap:6px}
.social span{width:25px;height:25px;border-radius:4px;background:#3a3a3a}
.copy{left:0;top:1180px;width:1088px;height:20px;background:#e0e0e0;padding:4px 0 0 151px;font-size:9px}
</style>
</head>
<body>
<header>
  <div class="abs topbar"></div>
  <div class="abs login"><strong>Register / Log In</strong><span>Lorem ipsum dolor sit amet, consectetuer adipiscing elit. Aenean commodo ligula eget dolor.</span></div>
  <div class="abs search">Search<svg width="14" height="14" viewBox="0 0 14 14"><circle cx="6" cy="6" r="4.3" fill="none" stroke="#555" stroke-width="2"/><line x1="9" y1="9" x2="13" y2="13" stroke="#555" stroke-width="2.4"/></svg></div>
  <div class="abs hero"></div>
  <div class="abs photo" role="img" aria-label="Photo of medical staff in a bright clinic corridor"></div>
  <div class="abs panel"></div>
  <div class="abs logo-cap"></div>
  <div class="abs brand"><i></i>Veranta</div>
  <nav>
    <div class="abs nav" style="top:131px">ABOUT US<svg width="18" height="18"><circle cx="9" cy="9" r="8" fill="#ddd" stroke="#888"/><path d="M7 5l4 4-4 4" stroke="#555" stroke-width="2" fill="none"/></svg></div>
    <div class="abs nav" style="top:173px">VIP CLUB<svg width="18" height="18"><circle cx="9" cy="9" r="8" fill="#ddd" stroke="#888"/><path d="M7 5l4 4-4 4" stroke="#555" stroke-width="2" fill="none"/></svg></div>
    <div class="abs nav" style="top:215px">PACKAGES AND PRICES<svg width="18" height="18"><circle cx="9" cy="9" r="8" fill="#ddd" stroke="#888"/><path d="M7 5l4 4-4 4" stroke="#555" stroke-width="2" fill="none"/></svg></div>
    <div class="abs nav" style="top:257px">CONTACT US<svg width="18" height="18"><circle cx="9" cy="9" r="8" fill="#ddd" stroke="#888"/><path d="M7 5l4 4-4 4" stroke="#555" stroke-width="2" fill="none"/></svg></div>
  </nav>
  <div class="abs strip"></div>
  <div class="abs connect"><i></i>Connect with Social</div>
  <div class="abs dot-blue"></div>
</header>

<section class="abs services">
  <div class="svc">Emergeny Services<br>Plan Covers.<div class="ico" role="img" aria-label="Heart monitor icon" style="background:linear-gradient(#d0d0d0,#8a8a8a)"></div></div>
  <div class="svc">Transportation<br>Services<div class="ico" role="img" aria-label="Ambulance icon" style="background:linear-gradient(#f4f4f4,#d46060)"></div></div>
  <div class="svc">Hotel Services<div class="ico" role="img" aria-label="Hospital building icon" style="background:linear-gradient(#e8eef6,#9fb2c8)"></div></div>
  <div class="svc">Variety of Doctors<div class="ico" role="img" aria-label="Doctor icon" style="background:linear-gradient(#eef2f6,#b9c9da)"></div></div>
  <div class="svc">Become a Member<div class="ico" role="img" aria-label="Medical clipboard icon" style="background:linear-gradient(#eee,#555)"></div></div>
</section>

<main>
  <h2 class="abs h2" style="left:154px;top:500px">Welcome to our website</h2>
  <div class="abs rule" style="left:136px;top:520px;width:261px"></div>
  <p class="abs lead" style="left:154px;top:537px;width:470px">Lorem ipsum dolor sit amet, consectetuer adipiscing elit. Aenean commodo ligula eget dolor. Aenean massa.</p>
  <p class="abs" style="left:154px;top:571px;width:470px">Aenean commodo ligula eget dolor. Aenean massa. Cum sociis natoque penatibus et magnis dis parturient montes, nascetur ridiculus mus. Donec quam felis, ultricies nec, pellentesque eu, pretium quis, sem.</p>
  <p class="abs" style="left:154px;top:605px;width:470px">Nulla consequat massa quis enim. Donec pede justo, fringilla vel, aliquet nec, vulputate eget, arcu. In enim justo, rhoncus ut, imperdiet a, venenatis vitae, justo. Nullam dictum felis eu pede mollis pretium. Integer tincidunt. Cras dapibus. Vivamus elementum semper nisi. Aenean vulputate eleifend tellus.</p>

  <h2 class="abs h2" style="left:154px;top:670px">Lorenm Ipsum Dolor</h2>
  <div class="abs rule" style="left:136px;top:693px;width:247px"></div>
  <p class="abs" style="left:165px;top:710px;width:200px">Lorem ipsum dolor sit amet, consectetuer adipiscing elit. Aenean commodo ligula eget dolor.</p>
  <p class="abs" style="left:165px;top:751px;width:200px">Lorem ipsum dolor sit amet, consectetuer adipiscing elit. Aenean commodo ligula eget dolor.</p>
  <p class="abs" style="left:415px;top:710px;width:200px">Lorem ipsum dolor sit amet, consectetuer adipiscing elit. Aenean commodo ligula eget dolor.</p>
  <p class="abs" style="left:415px;top:751px;width:200px">Lorem ipsum dolor sit amet, consectetuer adipiscing elit. Aenean commodo ligula eget dolor.</p>

  <h2 class="abs h2" style="left:691px;top:500px">Latest News</h2>
  <div class="abs rule" style="left:691px;top:521px;width:261px"></div>
  <div class="abs" style="left:692px;top:537px;width:245px">
    <div class="news-name">Jhon Doe</div><div>Posted on 12-01-2012</div>
    <p style="margin-top:6px">Lorem ipsum dolor sit amet, consectetuer adipiscing elit. Aenean commodo ligula eget dolor. Aenean massa. Cum sociis natoque penatibus et magnis dis parturient montes, nascetur ridiculus mus.</p>
    <div class="news-name" style="margin-top:6px">Jhon Doe</div><div>Posted on 12-01-2012</div>
    <p style="margin-top:6px">Lorem ipsum dolor sit amet, consectetuer adipiscing elit. Aenean commodo ligula eget dolor. Aenean massa. Cum sociis natoque penatibus et magnis dis parturient montes, nascetur ridiculus mus.</p>
  </div>
  <div class="abs" style="left:882px;top:721px;font-weight:700">read more</div>

  <div class="abs subhead" style="left:691px;top:752px;font-size:18px">Subscribe us</div>
  <div class="abs" style="left:691px;top:774px;font-size:8.5px">Exclusive deals delivered every day</div>
  <div class="abs email">enter your email here<i></i></div>
  <div class="abs" style="left:692px;top:817px;font-size:8.5px">unsubscribe us click here</div>
  <div class="abs apply">Appy</div>

  <h2 class="abs h2" style="left:171px;top:834px">See Our Service</h2>
  <div class="abs" style="left:136px;top:860px;width:816px;height:6px;background:var(--blue-rule)"></div>
  <svg class="abs arrow" style="left:140px;top:919px" viewBox="0 0 19 19"><circle cx="9.5" cy="9.5" r="8.5" fill="#ddd" stroke="#999"/><path d="M11 5l-4 4.5 4 4.5" stroke="#555" stroke-width="2" fill="none"/></svg>
  <div class="abs gallery">
    <div role="img" aria-label="Hospital emergency entrance" style="background:linear-gradient(#a9c3e0,#c58a7c 60%,#5b6b4a)"></div>
    <div role="img" aria-label="In-flight cabin service" style="background:linear-gradient(135deg,#e8e8ea,#7b7d86 60%,#2b2b33)"></div>
    <div role="img" aria-label="Hotel room with beds" style="background:linear-gradient(#f2e6a0,#d7a24a 60%,#a55f24)"></div>
    <div role="img" aria-label="In-flight cabin service" style="background:linear-gradient(135deg,#e8e8ea,#7b7d86 60%,#2b2b33)"></div>
    <div role="img" aria-label="Hotel room with beds" style="background:linear-gradient(#f2e6a0,#d7a24a 60%,#a55f24)"></div>
  </div>
  <svg class="abs arrow" style="left:927px;top:921px" viewBox="0 0 19 19"><circle cx="9.5" cy="9.5" r="8.5" fill="#ddd" stroke="#999"/><path d="M8 5l4 4.5-4 4.5" stroke="#555" stroke-width="2" fill="none"/></svg>
  <div class="abs" style="left:164px;top:981px;font-size:8px">Click images to enlarge</div>
</main>

<footer>
  <div class="abs footer"></div>
  <div class="abs subhead fh" style="left:151px;top:1018px">More About US</div>
  <p class="abs" style="left:152px;top:1041px;width:180px">Lorem ipsum dolor sit amet, consectetuer adipiscing elit. Aenean commodo ligula eget dolor. Aenean massa. Cum sociis natoque penatibus et magnis dis</p>
  <div class="abs subhead fh" style="left:150px;top:1096px">Lorem Ipsum</div>
  <div class="abs" style="left:154px;top:1111px;font-size:8.5px;line-height:1.35">insert Link<br>insert Link<br>insert Link<br>insert Link<br>insert Link</div>
  <div class="abs subhead fh" style="left:424px;top:1016px">Why Veranta</div>
  <p class="abs" style="left:424px;top:1040px;width:130px">Lorem ipsum dolor sit amet, consectetuer adipiscing elit. Aenean commodo ligula eget dolor. Aenean massa. Cum sociis natoque penatibus et magnis dis</p>
  <div class="abs subhead fh" style="left:632px;top:1015px">Contact Us</div>
  <p class="abs" style="left:635px;top:1041px;width:135px">Placeholder Ave 18,<br>Springdale<br>2040<br><br>Phone &nbsp;555-0142-780<br>Email :<br>dolor@verantasupport.com</p>
  <div class="abs" style="left:842px;top:1036px;display:flex;align-items:center;gap:5px;color:#666;font-weight:700;font-size:18px"><i style="display:block;width:10px;height:10px;border-radius:50%;background:#666"></i>Veranta</div>
  <div class="abs" style="left:834px;top:1073px;font-size:9.5px">Stay Connected to us on :</div>
  <div class="abs social" style="left:835px;top:1090px"><span></span><span></span><span></span><span></span></div>
  <div class="abs copy">Copyright veranta-club.com All Right Reserved 2011</div>
</footer>
</body>
</html>
```